Business Card Design

We need a business card design for a new company. We produce and sell fully grown topiary (please Google topiary pictures if you are not familiar with Topiary).We make many different topiary designs and shapes in all sizes. Ranging from cute little table top animal sculptures such as bunnies and swans for the indoors, to big sculptures such as actual size elephants for outdoor gardens and parks. We also make topiary balls, spiral shapes and other attractive geometrical shapes for indoor and outdoor decorations. We want to see designs that reflects the playfulness and ,liveliness and cute characteristics of our products.Please find attached the logo.Thank you

Industry/Entity Type

Business

Contact Information for Business Card

Company Name : Leaf Lark
Slogan : growing joy in every leaf
Tagline: Hedges...and beyond
Website : www.leaflark.example

Name on Card : Yusuf Tarek Mansour
Title : Founder & CEO
email: yusuf_tarek@leaflark.example

Address : 27 El-Borsaly Street
First Floor,Unit 4
Sahel Oasis,Giza,Egypt

Office Telephone : (02) 35908176
Mobile Number : 01062719048

Requirements
Must have
• The business card must have a white background.

```html
<!DOCTYPE html>
<html lang="en">
<head>
<meta charset="utf-8">
<title>Leaf Lark — Business Card</title>
<link rel="stylesheet" href="https://fonts.googleapis.com/css2?family=Arimo:wght@400;700&family=Patrick+Hand&family=Dancing+Script:wght@500&display=swap">
<style>
  :root {
    --leaf-green: #6aa33f;
    --deep-green: #5b9437;
    --swoosh-grey: #5f6163;
    --ink: #3a3a3a;
    --paper: #ffffff;
    --backdrop: #e9e7e2;
  }
  html, body {
    margin: 0;
    width: 1200px;
    height: 834px;
    overflow: hidden;
    background: var(--backdrop);
  }
  .card {
    position: absolute;
    left: 92px;
    top: 59px;
    width: 1019px;
    height: 689px;
    background: var(--paper);
    overflow: hidden;
    box-shadow: 0 4px 18px rgba(0,0,0,.15);
    font-family: "Arimo", Arial, sans-serif;
  }
  .card__waves {
    position: absolute;
    inset: 0;
    width: 100%;
    height: 100%;
  }
  .brand {
    position: absolute;
    left: 60px;
    top: 58px;
    display: flex;
    align-items: center;
    gap: 14px;
  }
  .brand__dot {
    width: 30px;
    height: 30px;
    border-radius: 50%;
    background: var(--leaf-green);
  }
  .brand__name {
    font-size: 100px;
    font-weight: 400;
    color: var(--leaf-green);
    line-height: 1;
  }
  .brand__slogan {
    position: absolute;
    left: 158px;
    top: 186px;
    margin: 0;
    font-family: "Patrick Hand", cursive;
    font-size: 35px;
    line-height: 1.2;
    color: var(--deep-green);
  }
  .brand__tagline {
    position: absolute;
    left: 185px;
    top: 236px;
    margin: 0;
    font-family: "Dancing Script", cursive;
    font-size: 36px;
    line-height: 1.2;
    color: var(--deep-green);
    letter-spacing: 1px;
  }
  .person {
    position: absolute;
    left: 61px;
    top: 322px;
    margin: 0;
    font-size: 33px;
    line-height: 1.2;
    color: var(--ink);
  }
  .person__name { color: var(--deep-green); font-weight: 700; }
  .contacts {
    position: absolute;
    left: 64px;
    top: 388px;
    margin: 0;
    padding: 0;
    list-style: none;
    font-size: 27px;
    color: var(--ink);
  }
  .contacts__item {
    display: flex;
    align-items: center;
    gap: 10px;
    height: 42px;
  }
  .contacts__icon { width: 20px; height: 20px; flex: none; }
  .address {
    position: absolute;
    right: 33px;
    top: 544px;
    margin: 0;
    font-style: normal;
    text-align: right;
    font-size: 26px;
    line-height: 37px;
    color: var(--paper);
  }
</style>
</head>
<body>
  <main class="card">
    <svg class="card__waves" viewBox="0 0 1019 689" aria-hidden="true">
      <path d="M0,0 L150,0 C80,15 25,60 0,118 Z" fill="var(--leaf-green)"/>
      <path d="M0,150 C30,75 110,20 225,4 C125,30 45,80 10,150 Z" fill="var(--swoosh-grey)"/>
      <path d="M0,672 C330,720 680,520 1019,456 L1019,689 L0,689 Z" fill="var(--leaf-green)"/>
      <path d="M0,550 C40,640 220,676 420,672 C210,666 60,640 0,585 Z" fill="var(--swoosh-grey)"/>
      <path d="M110,668 C430,660 740,520 1019,478" fill="none" stroke="var(--paper)" stroke-width="3"/>
    </svg>

    <header>
      <div class="brand">
        <span class="brand__dot"></span>
        <span class="brand__name">Leaf Lark</span>
      </div>
      <p class="brand__slogan">growing joy in every leaf</p>
      <p class="brand__tagline">Hedges...and beyond</p>
    </header>

    <p class="person"><span class="person__name">Yusuf Tarek Mansour,</span> Founder &amp; CEO</p>

    <ul class="contacts">
      <li class="contacts__item">
        <svg class="contacts__icon" viewBox="0 0 22 22"><rect x="6" y="1" width="10" height="20" rx="2" fill="var(--deep-green)"/><rect x="8" y="4" width="6" height="8" fill="#fff"/></svg>
        01062719048
      </li>
      <li class="contacts__item">
        <svg class="contacts__icon" viewBox="0 0 22 22"><path d="M5,2 L9,2 L10,7 L7,9 C8,12 10,14 13,15 L15,12 L20,13 L20,17 C20,19 18,20 16,20 C9,19 3,13 2,6 C2,4 3,2 5,2 Z" fill="var(--deep-green)"/></svg>
        (02) 35908176
      </li>
      <li class="contacts__item">
        <svg class="contacts__icon" viewBox="0 0 22 22"><rect x="1" y="5" width="20" height="13" rx="2" fill="var(--deep-green)"/><path d="M2,6 L11,13 L20,6" fill="none" stroke="#fff" stroke-width="1.6"/></svg>
        yusuf_tarek@leaflark.example
      </li>
      <li class="contacts__item">
        <svg class="contacts__icon" viewBox="0 0 22 22"><circle cx="11" cy="11" r="9" fill="var(--deep-green)"/><path d="M2,11 H20 M11,2 C6,6 6,16 11,20 M11,2 C16,6 16,16 11,20" fill="none" stroke="#fff" stroke-width="1.3"/></svg>
        www.leaflark.example
      </li>
    </ul>

    <address class="address">
      27 El-Borsaly Street<br>
      First Floor,Unit 4<br>
      Sahel Oasis,Giza,Egypt
    </address>
  </main>
</body>
</html>
```